Lifecoach needs website design based on a standard Wordpress theme

I need a website for my new lifecoaching business that can be easily implemented in Wordpress, it needs to be compatible with a standard Wordpress theme. So I can place the pictures, texts etc. in a standard theme of Wordpress.

I want the design to be a very good feeling and playfull one, based on my logo.

Target Market(s)

I will coach people to reach their goals and dreams in life.

Industry/Entity Type

Business

Requirements
Must have
• Can be easy implemented in Wordpress.
Nice to have
• Photo's of nature are nice.

```html
<!DOCTYPE html>
<html lang="en">
<head>
<meta charset="utf-8">
<title>Tom van Dijk – Lifecoach</title>
<link href="https://fonts.googleapis.com/css2?family=Noto+Serif&family=Raleway:wght@400;500;600&display=swap" rel="stylesheet">
<style>
:root{
  --header-bg:#eef1f3;
  --page-bg:#e4eaed;
  --navy:#034c7c;
  --brand:#0e5b8f;
  --nav-top:#6aa3c4;
  --nav-bottom:#4f87ab;
  --accent:#3aa0d9;
  --ink:#1f1f1f;
  --muted:#333;
  --card:#ffffff;
  --slide-top:#2f8fd0;
  --slide-bottom:#7fbde6;
  --btn-blue:#0b5fc4;
  --btn-teal:#3aa3cc;
  --btn-green:#56a94b;
  --btn-orange:#f59e23;
}
*{box-sizing:border-box;margin:0;padding:0}
html,body{width:1200px;height:1182px;overflow:hidden}
body{position:relative;background:var(--page-bg);font-family:"Raleway",Arial,sans-serif;color:var(--muted)}

.site-header{position:absolute;left:0;top:0;width:1200px;height:384px;background:radial-gradient(circle at 60% 30%,#f6f8f9,var(--header-bg) 70%)}
.brand{position:absolute;left:148px;top:42px;display:flex;align-items:center;gap:26px}
.brand-circle{width:196px;height:196px;border-radius:50%;border:10px solid var(--brand)}
.brand-name{font-family:"Noto Serif",Georgia,serif;font-weight:400;color:var(--brand);text-transform:uppercase;text-align:center;line-height:1.1}
.brand-name .line1{display:block;font-size:62px;letter-spacing:2px}
.brand-name .line2{display:block;font-size:38px;letter-spacing:2px;margin-top:2px}

.social{position:absolute;left:680px;top:278px;display:flex;gap:14px;align-items:center}
.social span{font-size:14px;font-weight:600;color:var(--brand)}

.search{position:absolute;left:857px;top:271px;width:229px;height:35px;border:2px solid var(--brand);border-radius:18px;background:#fff;overflow:hidden;display:flex}
.search span{flex:1;padding:7px 10px;font-size:14px;color:#333}
.search button{width:42px;border:0;background:#3d6f97;display:flex;align-items:center;justify-content:center}

.main-nav{position:absolute;left:127px;top:326px;width:961px;height:35px;border-radius:18px;background:linear-gradient(var(--nav-top),var(--nav-bottom));box-shadow:0 2px 3px rgba(0,0,0,.2);display:flex;align-items:center;padding-left:34px;gap:29px}
.main-nav a{color:#fff;font-size:14px;font-weight:600;text-decoration:none;text-shadow:0 1px 1px rgba(0,0,0,.25)}
.main-nav a.drop::after{content:"";display:inline-block;width:5px;height:5px;border-right:2px solid #fff;border-bottom:2px solid #fff;transform:rotate(45deg);margin:0 0 3px 5px}

.slider-band{position:absolute;left:0;top:384px;width:1200px;height:431px;background:var(--navy)}
.slider-band::after{content:"";position:absolute;left:130px;right:115px;bottom:-14px;height:14px;background:radial-gradient(ellipse at top,rgba(0,0,0,.35),transparent 70%)}
.slider-frame{position:absolute;left:137px;top:22px;width:940px;height:386px;background:#fff;border-radius:6px}
.slide{position:absolute;left:16px;top:16px;width:907px;height:353px;border:3px solid var(--accent);border-radius:4px;background:linear-gradient(var(--slide-top),var(--slide-bottom))}
.arrow{position:absolute;top:204px;width:42px;height:42px;border-radius:50%;background:#f3f5f6;box-shadow:0 1px 3px rgba(0,0,0,.4);display:flex;align-items:center;justify-content:center}
.arrow.prev{left:98px}.arrow.next{left:1074px}

.post{position:absolute;left:139px;top:862px;width:616px;height:330px;background:var(--card);border-left:3px solid var(--accent);padding:26px 25px}
.post h1{font-family:"Noto Serif",Georgia,serif;font-weight:400;font-size:34px;line-height:41px;color:var(--ink)}
.comments{position:absolute;right:28px;top:29px;width:33px;height:33px;border:2px solid #bbb;border-radius:6px;background:#f3f3f3;text-align:center;font:600 24px/29px Arial,sans-serif;color:#555}
.meta{display:flex;gap:16px;font-size:14px;margin-top:37px;align-items:center}
.meta span{display:flex;align-items:center;gap:8px}
.post p{margin-top:23px;font-family:Arial,sans-serif;font-size:14px;line-height:17px;color:#111}
.post-image{position:absolute;left:25px;top:240px;width:560px;height:90px;background:linear-gradient(#1f73b8,#5aa6dc)}

.sidebar{position:absolute;left:779px;top:862px;width:296px;height:314px;background:var(--card);border-left:3px solid var(--accent);padding:22px 24px}
.sidebar h2{font-family:"Noto Serif",Georgia,serif;font-weight:400;font-size:36px;color:var(--ink);line-height:42px}
.buttons{margin-top:14px;margin-left:10px;display:flex;flex-direction:column;gap:19px}
.btn{width:152px;height:27px;border-radius:3px;font-size:13px;line-height:25px;text-align:center;color:#fff;border:1px solid rgba(0,0,0,.15)}
.btn.plain{background:#f7f7f7;color:#333;border-color:#ccc}
.btn.blue{background:var(--btn-blue)}.btn.teal{background:var(--btn-teal)}.btn.green{background:var(--btn-green)}.btn.orange{background:var(--btn-orange)}
</style>
</head>
<body>
<header class="site-header">
  <div class="brand">
    <div class="brand-circle"></div>
    <div class="brand-name"><span class="line1">Tom van Dijk</span><span class="line2">Lifecoach</span></div>
  </div>
  <div class="social"><span>Linkup</span><span>Chirp</span><span>Plusly</span></div>
  <div class="search"><span>Search...</span><button aria-label="Search"><svg width="18" height="18" viewBox="0 0 18 18"><circle cx="10" cy="7" r="5" fill="none" stroke="#fff" stroke-width="2"/><line x1="6.5" y1="10.5" x2="2" y2="15" stroke="#fff" stroke-width="2.5"/></svg></button></div>
  <nav class="main-nav">
    <a>Blog / home</a><a>Features</a><a class="drop">Page samples</a><a>Gallery</a><a class="drop">Custom pages</a><a class="drop">Slider</a><a>Contact</a><a>E-commerce</a>
  </nav>
</header>

<section class="slider-band">
  <div class="slider-frame">
    <div class="slide" role="img" aria-label="Slider photo: a joyful person with colourful balloons in a sunny meadow"></div>
  </div>
  <div class="arrow prev"><svg width="16" height="20" viewBox="0 0 16 20"><path d="M11 3 L4 10 L11 17" fill="none" stroke="#3aa0d9" stroke-width="4" stroke-linecap="round"/></svg></div>
  <div class="arrow next"><svg width="16" height="20" viewBox="0 0 16 20"><path d="M5 3 L12 10 L5 17" fill="none" stroke="#3aa0d9" stroke-width="4" stroke-linecap="round"/></svg></div>
</section>

<article class="post">
  <h1>Tom van Dijk<br>- your lifecoach</h1>
  <div class="comments">0</div>
  <div class="meta">
    <span><svg width="16" height="16" viewBox="0 0 16 16"><circle cx="8" cy="5" r="3.5" fill="#3d6f97"/><path d="M1 15 Q8 5 15 15Z" fill="#3d6f97"/></svg>By admin</span>
    <span><svg width="14" height="14" viewBox="0 0 14 14"><rect x="1" y="2" width="12" height="11" fill="none" stroke="#555"/><line x1="1" y1="5" x2="13" y2="5" stroke="#555"/></svg>On May 21, 2013</span>
    <span><svg width="16" height="14" viewBox="0 0 16 14"><path d="M1 2 H6 L7 4 H15 V13 H1Z" fill="#3d6f97"/></svg>Uncategorized</span>
  </div>
  <p>Lorem ipsum dolor sit amet, consectetuer adipiscing elit, sed diam nonummy nibh euismod tincidunt ut laoreet dolore magna aliquam erat volutpat.</p>
  <div class="post-image" role="img" aria-label="Post photo: colourful balloons against a blue sky"></div>
</article>

<aside class="sidebar">
  <h2>Testing</h2>
  <div class="buttons">
    <div class="btn plain">Click here for Findly!</div>
    <div class="btn blue">Click here for Findly!</div>
    <div class="btn teal">Click here for Findly!</div>
    <div class="btn green">Click here for Findly!</div>
    <div class="btn orange">Click here for Findly!</div>
  </div>
</aside>
</body>
</html>
```